Tolvane Handyman Service

File 2 Prep kitchen cabinets
File 3 Painting kitchen cabinets
File 4 Demo stairs
File 5 Completion Installing stair treads
File 6 Power washing deck
File 7 Completion of Sainting deck and railings
File 8 Completion of staining steps
Logo, owner name, email and web site on front cover
File 9 Demo living room floor
File 10 Completion of living room floor
Please see additional on attached flyer

Target Market(s)

Residential

Industry/Entity Type

Painting

Font styles to use
Serif
Sans Serif

Requirements
Must have
• Some Photos and type of work discerption
Front page Logo, web address, phone number, owners name and email address
Back Page see attached file 1
Nice to have
• Photo maybe in middle of flyer
Use the best text that you think will meet the needs
Should not have
• No pink colors

```html
<!DOCTYPE html>
<html lang="en">
<head>
<meta charset="utf-8">
<title>Tolvane Handyman Services – Mailer</title>
<link href="https://fonts.googleapis.com/css2?family=Arimo:wght@400;700&family=Oswald:wght@300;500;600&family=Roboto+Slab:wght@800&display=swap" rel="stylesheet">
<style>
  :root{
    --brand-blue:#3e5fa6;
    --band-grey:#a4a5a8;
    --paper:#f3f3f3;
    --white:#ffffff;
    --ink:#333333;
    --backdrop:#1c1c1c;
  }
  *{box-sizing:border-box;margin:0;padding:0}
  html,body{width:1200px;height:921px;overflow:hidden;background:var(--backdrop)}
  .mailer{position:absolute;left:91px;top:67px;width:1018px;height:786px;background:var(--paper);overflow:hidden;font-family:"Arimo",Arial,sans-serif}

  /* ---------- left panel ---------- */
  .panel-left{position:absolute;left:0;top:0;width:340px;height:786px;background:var(--white)}
  .band-grey{position:absolute;left:0;top:0;width:340px;height:98px;background:var(--band-grey)}
  .band-blue{position:absolute;left:0;top:98px;width:340px;height:248px;background:var(--brand-blue)}
  .callout-frame{position:absolute;left:0;top:0;width:340px;height:346px}
  .kicker{position:absolute;left:43px;top:64px;font-family:"Oswald",sans-serif;font-weight:600;font-size:31px;line-height:1;color:var(--white);letter-spacing:-0.2px}
  .slogan{position:absolute;left:46px;top:101px;list-style:none;color:var(--white);font-weight:700;font-size:44px;line-height:51.5px}
  .benefits{position:absolute;left:53px;top:374px;list-style:none;color:var(--ink);font-size:22px;line-height:31px}
  .benefits li{display:flex;align-items:center;gap:12px}
  .benefits svg{width:9px;height:9px;flex:none}
  .photo-stairs{position:absolute;left:0;top:505px;width:340px;height:197px;background:linear-gradient(160deg,#d9d6cf 0%,#b9a98c 55%,#8d7a5d 100%)}
  .contact-bar{position:absolute;left:0;top:656px;width:340px;height:46px;background:rgba(240,240,240,.9);padding:6px 0 0 48px}
  .contact-label{font-size:13px;color:var(--ink);line-height:15px}
  .contact-owner{font-size:20px;font-weight:700;color:var(--brand-blue);line-height:22px}
  .contact-list{position:absolute;left:47px;top:712px;list-style:none;font-size:14px;color:var(--ink);line-height:19.5px}
  .contact-list li{display:flex;align-items:center;gap:12px}
  .contact-list svg{width:15px;height:15px;flex:none}

  /* ---------- middle + right ---------- */
  .sweeps{position:absolute;left:0;top:0;width:1018px;height:786px}
  .return-address{position:absolute;left:613px;top:26px;height:180px;writing-mode:vertical-rl;color:var(--white);font-size:13.5px;line-height:15px}
  .return-address strong{font-weight:700}
  .address-lines{position:absolute;left:369px;top:461px;width:150px;height:306px}
  .stamp-box{position:absolute;left:584px;top:695px;width:81px;height:76px;border:4px solid var(--white)}

  .brand-name{position:absolute;left:679px;top:146px;width:339px;text-align:center;font-family:"Roboto Slab",serif;font-weight:800;font-size:16px;color:#111}
  .brand-tag{position:absolute;left:679px;top:166px;width:339px;text-align:center;font-family:"Roboto Slab",serif;font-weight:800;font-size:15px;color:var(--brand-blue)}
  .brand-mark{position:absolute;left:820px;top:84px;width:56px;height:56px;border:6px solid var(--brand-blue)}

  .work-photo{position:absolute;width:112px;height:112px;border-radius:50%;border:3px solid var(--white)}
  .work-deck{left:884px;top:193px;background:radial-gradient(circle at 40% 40%,#9a6b45,#6d4a30)}
  .work-treads{left:777px;top:271px;background:radial-gradient(circle at 50% 50%,#6a5a4c,#d9d6d0)}
  .work-railing{left:696px;top:375px;background:radial-gradient(circle at 50% 40%,#f2f2f2,#7f8d72)}

  .headline{position:absolute;left:727px;top:536px;font-family:"Oswald",sans-serif;font-weight:500;font-size:32px;line-height:40px;color:var(--white)}
  .service-area{position:absolute;left:727px;top:634px;font-family:"Oswald",sans-serif;font-weight:300;font-style:italic;font-size:25px;line-height:36px;color:var(--white)}
</style>
</head>
<body>
<main class="mailer">

  <section class="panel-left">
    <div class="band-grey"></div>
    <div class="band-blue"></div>
    <svg class="callout-frame" viewBox="0 0 340 346" aria-hidden="true">
      <path d="M239 313 H23 V38 H317 V313 H278 L250 346 M239 313 V346" fill="none" stroke="#fff" stroke-width="3"/>
    </svg>
    <p class="kicker">ONE CALL DOES IT ALL</p>
    <ul class="slogan">
      <li>FIX IT.</li>
      <li>REPAIR IT.</li>
      <li>CHANGE IT.</li>
      <li>BUILD IT.</li>
    </ul>
    <ul class="benefits">
      <li><svg viewBox="0 0 10 10"><path d="M1 5 L4 8 L9 2" fill="none" stroke="#333" stroke-width="2"/></svg>35 years Experience</li>
      <li><svg viewBox="0 0 10 10"><path d="M1 5 L4 8 L9 2" fill="none" stroke="#333" stroke-width="2"/></svg>Free Written Estimates</li>
      <li><svg viewBox="0 0 10 10"><path d="M1 5 L4 8 L9 2" fill="none" stroke="#333" stroke-width="2"/></svg>Fully Insured</li>
      <li><svg viewBox="0 0 10 10"><path d="M1 5 L4 8 L9 2" fill="none" stroke="#333" stroke-width="2"/></svg>Locally Owned</li>
    </ul>
    <div class="photo-stairs" role="img" aria-label="Staircase during demolition with worn treads and white balusters"></div>
    <div class="contact-bar">
      <p class="contact-label">Contact</p>
      <p class="contact-owner">Owner Dale Morrow</p>
    </div>
    <ul class="contact-list">
      <li><svg viewBox="0 0 16 16"><circle cx="8" cy="8" r="8" fill="#3e5fa6"/><path d="M5 4 L7 4 L7.5 6 L6.5 7 Q7.5 9 9 9.5 L10 8.5 L12 9 L12 11 Q7 12 4 6 Z" fill="#fff"/></svg>(207) 555-0148</li>
      <li><svg viewBox="0 0 16 16"><circle cx="8" cy="8" r="8" fill="#3e5fa6"/><path d="M4 8 L12 4.5 L10.5 12 L8 9.5 Z" fill="#fff"/></svg>dale@tolvanehandyman.com</li>
      <li><svg viewBox="0 0 16 16"><circle cx="8" cy="8" r="8" fill="#3e5fa6"/><ellipse cx="8" cy="8" rx="3" ry="6" fill="none" stroke="#fff"/><path d="M2.5 8 H13.5" stroke="#fff"/></svg>www.tolvanehandyman.com</li>
    </ul>
  </section>

  <svg class="sweeps" viewBox="0 0 1018 786" aria-hidden="true">
    <path d="M412 0 C510 80 640 260 679 497" fill="none" stroke="#fff" stroke-width="16"/>
    <path d="M422 0 H679 V497 C640 260 520 80 422 0 Z" fill="#3e5fa6"/>
    <path d="M679 420 C770 320 880 210 1018 130 V194 C880 260 760 420 679 554 Z" fill="#fff"/>
    <path d="M679 554 C760 420 880 260 1018 194 V786 H679 Z" fill="#3e5fa6"/>
  </svg>

  <p class="return-address"><strong>Tolvane Handyman Services</strong><br>18 B Harbor Mill Rd<br>Kennet, Maine 04000</p>

  <svg class="address-lines" viewBox="0 0 150 306" aria-hidden="true">
    <g stroke="#888" stroke-width="1" stroke-dasharray="1 3">
      <path d="M0 0 V306 M37 0 V306 M74 0 V306 M111 0 V306 M148 0 V306"/>
    </g>
  </svg>
  <div class="stamp-box"></div>

  <div class="brand-mark"></div>
  <p class="brand-name">Tolvane Handyman Services</p>
  <p class="brand-tag">Painting &amp; Remodeling</p>

  <div class="work-photo work-deck" role="img" aria-label="Freshly stained wooden deck"></div>
  <div class="work-photo work-treads" role="img" aria-label="Stairs with new dark treads and white risers"></div>
  <div class="work-photo work-railing" role="img" aria-label="Painted white deck railing and steps"></div>

  <h1 class="headline">We Are The Solution<br>To Your Problems!</h1>
  <p class="service-area">Serving Southern Maine For<br>All Your Painting And<br>Remodeling</p>

</main>
</body>
</html>
```